Website for Cedar Brook Fellowship Church

Wordpress website design required for Cedar Brook Fellowship Church. We are a family oriented church catering for age groups from school age to elderly people. The church has a wide variety of activities which it coordinates. The idea is to describe the activities on the activities page, but cross-link them to show which would be applicable to the different age groups.

We would like an inviting website which is easy to read and navigate.

Target Market(s)

Very wide audience - from school age youth to elderly people, so design and style should cater for both audiences.

Industry/Entity Type

Church

Coding

Coded - Design and coding required

Number of Pages Required

5+ page

Font styles to use
Sans Serif

Colors
0255a3
ffffff
0792cd
f78f20

Requirements
Must have
• Inviting website.
• Clear readable font.
• Space to import photos to balance text on each page.
• Need to project a dynamic and progressive feel for the church.
• Easy to navigate.
Nice to have
• Scrolling photos on pages. Ability to enter questions/ comments/prayer requests on Home page.
Should not have
• Conservative audience, so should not be too bold.

```html
<!DOCTYPE html>
<html lang="en">
<head>
<meta charset="utf-8">
<title>Cedar Brook Fellowship Church</title>
<link href="https://fonts.googleapis.com/css2?family=Raleway:wght@500;600;700&family=Open+Sans:ital,wght@0,400;0,600;0,700;1,400&display=swap" rel="stylesheet">
<style>
:root{
  --navy:#0255a3;
  --sky:#0792cd;
  --orange:#f78f20;
  --white:#ffffff;
  --ink:#222222;
  --muted:#777777;
  --news-bg:#e9edf2;
  --footer:#1b1b1b;
  --line:#3a3a3a;
}
*{margin:0;padding:0;box-sizing:border-box}
html,body{width:1200px;height:2225px;overflow:hidden}
body{position:relative;font-family:"Open Sans",Arial,sans-serif;color:var(--ink);background:var(--white)}
.abs{position:absolute}

/* header */
.top-rule{left:0;top:0;width:1200px;height:4px;background:var(--navy)}
.brand{left:98px;top:52px;display:flex;align-items:center;gap:8px;font-family:"Raleway",sans-serif;font-weight:600;font-size:15px;color:var(--navy)}
.brand-dot{width:12px;height:12px;border-radius:50%;background:var(--navy)}
.top-btn{top:16px;height:33px;display:flex;align-items:center;justify-content:center;gap:7px;color:var(--white);font-family:"Raleway",sans-serif;font-weight:700;font-size:14px;text-transform:uppercase;border-radius:2px}
.btn-calendar{left:654px;width:136px;background:var(--orange)}
.btn-contact{left:801px;width:136px;background:var(--navy)}
.btn-login{left:948px;width:152px;background:var(--sky)}
.main-nav{top:60px;font-family:"Raleway",sans-serif;font-weight:600;font-size:16px;color:#2a2a2a}
.main-nav.active{color:var(--orange)}

/* hero */
.hero{left:0;top:92px;width:1200px;height:442px;background:linear-gradient(100deg,#4a3c30 0%,#6b5a4a 30%,#54504a 55%,#3e3a36 80%,#2c2a28 100%)}
.hero-shade{left:0;top:92px;width:1200px;height:442px;background:rgba(0,0,0,.35)}
.hero-title{left:0;top:205px;width:1200px;text-align:center;color:var(--white);font-family:"Raleway",sans-serif;font-weight:700;font-size:52px;line-height:64px;text-shadow:0 2px 6px rgba(0,0,0,.4)}
.hero-quote{left:230px;top:273px;width:740px;text-align:center;color:var(--white);font-size:18.5px;line-height:29px;text-shadow:0 1px 4px rgba(0,0,0,.5)}
.hero-btn{left:500px;top:351px;width:200px;height:43px;background:var(--orange);color:var(--white);font-family:"Raleway",sans-serif;font-weight:700;font-size:16px;display:flex;align-items:center;justify-content:center;border-radius:2px}
.dots{left:558px;top:474px;display:flex;gap:4px}
.dot{width:18px;height:18px;border-radius:50%;border:2px solid var(--white)}
.dot.on{background:var(--white)}

/* welcome */
.welcome{left:0;top:534px;width:1200px;height:252px;background:var(--navy)}
.welcome-title{left:0;top:566px;width:1200px;text-align:center;color:var(--white);font-family:"Raleway",sans-serif;font-weight:700;font-size:28px}
.welcome-text{left:206px;top:612px;width:788px;text-align:center;color:var(--white);font-size:12.5px;line-height:23.5px}
.outline-btn{left:532px;top:706px;width:135px;height:40px;border:1.5px solid var(--white);border-radius:4px;color:var(--white);font-family:"Raleway",sans-serif;font-weight:700;font-size:14px;display:flex;align-items:center;justify-content:center}

/* activities */
.section-title{font-family:"Raleway",sans-serif;font-weight:700;font-size:27px;color:#2a2a2a}
.activities-title{left:0;top:832px;width:1200px;text-align:center}
.card{top:893px;width:239px}
.card-photo{width:239px;height:178px;border:3px solid #e3e3e3}
.card-title{margin-top:16px;font-family:"Raleway",sans-serif;font-weight:700;font-size:18px;color:#222;white-space:nowrap}
.card-text{margin-top:8px;font-size:12px;line-height:21.5px;color:var(--muted)}
.read-more{font-family:"Raleway",sans-serif;font-weight:700;font-size:13px;color:var(--orange)}
.card .read-more{display:block;margin-top:10px}
.slide-arrow{width:42px;height:42px;border-radius:50%;background:#dcdcdc;display:flex;align-items:center;justify-content:center}

/* news */
.news{left:0;top:1256px;width:1200px;height:279px;background:var(--news-bg)}
.news-title{left:99px;top:1290px;font-size:26px}
.news-arrow{top:1290px;width:34px;height:34px;border-radius:50%;background:#d2dbe6;display:flex;align-items:center;justify-content:center}
.news-item{top:1352px;width:490px;height:130px}
.news-photo{position:absolute;left:0;top:0;width:152px;height:117px;border:3px solid #fff;box-shadow:0 0 0 1px #d6d6d6}
.news-body{position:absolute;left:173px;top:0;width:320px}
.news-head{font-weight:700;font-size:14.5px;color:#222;text-transform:uppercase;letter-spacing:.2px;white-space:nowrap}
.news-meta{margin-top:7px;font-size:12px;font-style:italic;color:var(--navy);display:flex;gap:20px;align-items:center}
.news-meta span{display:flex;gap:6px;align-items:center}
.news-text{margin-top:9px;font-size:12px;line-height:22px;color:var(--muted);width:312px}
.news-body .read-more{display:block;margin-top:6px}

/* prayer + service */
.band{left:0;top:1535px;width:1200px;height:385px;background:var(--orange)}
.band-title{font-family:"Raleway",sans-serif;font-weight:700;font-size:25px;color:var(--white)}
.label{font-size:12px;color:var(--white)}
.field{background:var(--white);height:32px}
.submit{left:98px;top:1833px;width:586px;height:45px;background:linear-gradient(#1366b8,#024a91);border-radius:3px;color:var(--white);font-family:"Raleway",sans-serif;font-weight:700;font-size:16px;display:flex;align-items:center;justify-content:center}
.service-text{left:724px;top:1621px;width:380px;font-size:12px;line-height:20px;color:var(--white)}
.hours{left:724px;top:1686px;border-collapse:collapse;font-family:"Raleway",sans-serif;font-weight:700;font-size:15px;color:var(--white)}
.hours td{height:29.3px;padding:0}
.hours .day{width:124px}
.hours .sep{width:42px}

/* footer */
.footer{left:0;top:1920px;width:1200px;height:305px;background:var(--footer)}
.foot-brand{left:98px;top:1950px;width:190px;display:flex;flex-direction:column;align-items:center;gap:14px;text-align:center;color:var(--white);font-family:"Raleway",sans-serif;font-weight:700;font-size:17px;line-height:23px}
.foot-circle{width:70px;height:70px;border-radius:50%;background:var(--white)}
.vline{top:1952px;width:1px;height:180px;background:var(--line)}
.foot-head{top:1952px;font-family:"Raleway",sans-serif;font-weight:700;font-size:17px;color:var(--white)}
.foot-links{left:354px;top:1993px;list-style:none;font-size:12px;line-height:23.2px;color:#ddd}
.foot-text{font-size:12px;line-height:21px;color:#ddd}
.sub-input{left:549px;top:2044px;width:273px;height:32px;background:var(--white);font-size:11.5px;color:#666;padding-left:15px;display:flex;align-items:center}
.sub-btn{left:549px;top:2090px;width:101px;height:35px;border:2px solid var(--white);border-radius:4px;color:var(--white);font-family:"Raleway",sans-serif;font-weight:700;font-size:12.5px;display:flex;align-items:center;justify-content:center}
.contact-row{left:890px;display:flex;gap:16px;font-size:12px;line-height:21px;color:#ddd;white-space:nowrap}
.contact-row svg{flex:none;margin-top:3px}
.foot-rule{left:98px;top:2155px;width:1004px;height:1px;background:var(--line)}
.copyright{left:98px;top:2180px;font-size:12px;color:#ddd}
.social{top:2171px;width:34px;height:34px;border-radius:50%;border:2px solid var(--white)}
</style>
</head>
<body>

<!-- header -->
<div class="abs top-rule"></div>
<div class="abs brand"><span class="brand-dot"></span>Cedar Brook Fellowship Church</div>

<div class="abs top-btn btn-calendar">
  <svg width="13" height="13" viewBox="0 0 13 13"><rect x="1" y="2" width="11" height="10" fill="none" stroke="#fff" stroke-width="1.5"/><line x1="1" y1="5" x2="12" y2="5" stroke="#fff" stroke-width="1.5"/><line x1="4" y1="0.5" x2="4" y2="3" stroke="#fff" stroke-width="1.5"/><line x1="9" y1="0.5" x2="9" y2="3" stroke="#fff" stroke-width="1.5"/></svg>Calendar
</div>
<div class="abs top-btn btn-contact">
  <svg width="14" height="11" viewBox="0 0 14 11"><rect x="0.5" y="0.5" width="13" height="10" fill="#fff"/><path d="M0.5 0.5 L7 6 L13.5 0.5" fill="none" stroke="#0255a3" stroke-width="1.2"/></svg>Contact Us
</div>
<div class="abs top-btn btn-login">
  <svg width="12" height="13" viewBox="0 0 12 13"><circle cx="6" cy="3.5" r="3" fill="#fff"/><path d="M0.5 13 Q0.5 7 6 7 Q11.5 7 11.5 13 Z" fill="#fff"/></svg>Member Login
</div>

<nav>
  <span class="abs main-nav active" style="left:450px">Home</span>
  <span class="abs main-nav" style="left:523px">Age Group</span>
  <span class="abs main-nav" style="left:632px">Activites</span>
  <span class="abs main-nav" style="left:725px">Events Calendar</span>
  <span class="abs main-nav" style="left:876px">About CBFC</span>
  <span class="abs main-nav" style="left:1000px">Contact</span>
  <svg class="abs" style="left:1086px;top:62px" width="16" height="16" viewBox="0 0 16 16"><circle cx="6.5" cy="6.5" r="5" fill="none" stroke="#2a2a2a" stroke-width="2"/><line x1="10.3" y1="10.3" x2="15" y2="15" stroke="#2a2a2a" stroke-width="2.4"/></svg>
</nav>

<!-- hero -->
<div class="abs hero" role="img" aria-label="Photo of church members sharing a meal together at long tables"></div>
<div class="abs hero-shade"></div>
<h1 class="abs hero-title">Cedar Brook Fellowship Church</h1>
<p class="abs hero-quote">"Our mission is to reflect the love of God as revealed in Jesus and through<br>His Spirit to make him known by word, sign and deed"</p>
<div class="abs hero-btn">GET MORE INFO &gt;&gt;</div>
<div class="abs dots"><span class="dot on"></span><span class="dot"></span><span class="dot"></span><span class="dot"></span></div>

<!-- welcome -->
<section class="abs welcome"></section>
<h2 class="abs welcome-title">Welcome to Cedar Brook Fellowship Church</h2>
<p class="abs welcome-text">We hold two services which are at 8 am (traditional worship service where we sing hymns) and at 10 am (family worship service) where the children would head off to join the Micro Minis, Sunday Club or (Junior) Juice during the sermon. Holy Communion is generally held on the 3rd Sunday of the month. Our Minister is the Reverend Daniel Hartley.</p>
<div class="abs outline-btn">ABOUT CBFC</div>

<!-- activities -->
<h2 class="abs section-title activities-title">Church Activities</h2>
<div class="abs slide-arrow" style="left:56px;top:961px"><svg width="12" height="18" viewBox="0 0 12 18"><path d="M9 2 L3 9 L9 16" fill="none" stroke="#999" stroke-width="2"/></svg></div>
<div class="abs slide-arrow" style="left:1102px;top:961px"><svg width="12" height="18" viewBox="0 0 12 18"><path d="M3 2 L9 9 L3 16" fill="none" stroke="#999" stroke-width="2"/></svg></div>

<article class="abs card" style="left:98px">
  <div class="card-photo" role="img" aria-label="Photo of children gathered for prayer in the chapel" style="background:linear-gradient(135deg,#8c4b3c,#b87b5e 55%,#6f5a4e)"></div>
  <h3 class="card-title">Prayer Group</h3>
  <p class="card-text">We hold two services which are at 8 am (traditional worship service where we sing hymns) and at 10 am.</p>
  <span class="read-more">READ MORE &gt;&gt;</span>
</article>
<article class="abs card" style="left:353px">
  <div class="card-photo" role="img" aria-label="Photo of men chatting over coffee outdoors" style="background:linear-gradient(135deg,#5a6b3e,#a89a7a 50%,#7b6a55)"></div>
  <h3 class="card-title">Men Coffee Group</h3>
  <p class="card-text">We hold two services which are at 8 am (traditional worship service where we sing hymns) and at 10 am.</p>
  <span class="read-more">READ MORE &gt;&gt;</span>
</article>
<article class="abs card" style="left:608px">
  <div class="card-photo" role="img" aria-label="Photo of children around a candlelit table" style="background:linear-gradient(135deg,#6b4a3a,#b2433a 55%,#7a3a30)"></div>
  <h3 class="card-title">Koala Kids Playgroup</h3>
  <p class="card-text">We hold two services which are at 8 am (traditional worship service where we sing hymns) and at 10 am.</p>
  <span class="read-more">READ MORE &gt;&gt;</span>
</article>
<article class="abs card" style="left:863px">
  <div class="card-photo" role="img" aria-label="Photo of a meditation group gathered in a lounge room" style="background:linear-gradient(135deg,#9a8f86,#c7b9a8 50%,#8a7c70)"></div>
  <h3 class="card-title">Christian Meditation Group</h3>
  <p class="card-text">We hold two services which are at 8 am (traditional worship service where we sing hymns) and at 10 am.</p>
  <span class="read-more">READ MORE &gt;&gt;</span>
</article>

<!-- news -->
<section class="abs news"></section>
<h2 class="abs section-title news-title">Our News</h2>
<div class="abs news-arrow" style="left:1031px"><svg width="10" height="14" viewBox="0 0 10 14"><path d="M7 2 L3 7 L7 12" fill="none" stroke="#0255a3" stroke-width="2"/></svg></div>
<div class="abs news-arrow" style="left:1068px"><svg width="10" height="14" viewBox="0 0 10 14"><path d="M3 2 L7 7 L3 12" fill="none" stroke="#0255a3" stroke-width="2"/></svg></div>

<article class="abs news-item" style="left:101px">
  <div class="news-photo" role="img" aria-label="Photo of two church members talking" style="background:linear-gradient(135deg,#6e4a42,#a88e7c 50%,#4e5a4a)"></div>
  <div class="news-body">
    <h3 class="news-head">What's wrong with a little sledging?</h3>
    <div class="news-meta">
      <span><svg width="11" height="11" viewBox="0 0 11 11"><rect x="0.5" y="1.5" width="10" height="9" fill="#0255a3"/></svg>20/10/2016</span>
      <span><svg width="10" height="11" viewBox="0 0 10 11"><circle cx="5" cy="3" r="2.6" fill="#0255a3"/><path d="M0 11 Q0 6 5 6 Q10 6 10 11Z" fill="#0255a3"/></svg>cbfcadmin</span>
    </div>
    <p class="news-text">Many decades ago, in the last century, I played cricket. I think they were short on numbers.</p>
    <span class="read-more">READ MORE &gt;&gt;</span>
  </div>
</article>
<article class="abs news-item" style="left:619px">
  <div class="news-photo" role="img" aria-label="Photo of a congregation seated at a community lunch" style="background:linear-gradient(135deg,#3c3a3e,#8a7e78 50%,#5a4a44)"></div>
  <div class="news-body">
    <h3 class="news-head">Monthly Mail October 2016</h3>
    <div class="news-meta">
      <span><svg width="11" height="11" viewBox="0 0 11 11"><rect x="0.5" y="1.5" width="10" height="9" fill="#0255a3"/></svg>05/10/2016</span>
      <span><svg width="10" height="11" viewBox="0 0 10 11"><circle cx="5" cy="3" r="2.6" fill="#0255a3"/><path d="M0 11 Q0 6 5 6 Q10 6 10 11Z" fill="#0255a3"/></svg>cbfcadmin</span>
    </div>
    <p class="news-text">Many decades ago, in the last century, I played cricket. I think they were short on numbers.</p>
    <span class="read-more">READ MORE &gt;&gt;</span>
  </div>
</article>

<!-- prayer request + service times -->
<section class="abs band"></section>
<h2 class="abs band-title" style="left:98px;top:1570px">Prayer request Form</h2>
<span class="abs label" style="left:98px;top:1619px">Name :</span>
<span class="abs label" style="left:400px;top:1619px">Email :</span>
<div class="abs field" style="left:98px;top:1642px;width:288px"></div>
<div class="abs field" style="left:397px;top:1642px;width:287px"></div>
<span class="abs label" style="left:98px;top:1681px">Phone :</span>
<div class="abs field" style="left:98px;top:1702px;width:586px"></div>
<span class="abs label" style="left:98px;top:1742px">Prayer Requests :</span>
<div class="abs field" style="left:98px;top:1762px;width:586px;height:56px"></div>
<div class="abs submit">SUBMIT</div>

<h2 class="abs band-title" style="left:724px;top:1570px">Service times</h2>
<p class="abs service-text">At vero eos et accusamus et iusto odio dignissimos ducimus qblan<br>ditiis praesentium voluptatum deleniti atque.</p>
<table class="abs hours">
  <tr><td class="day">Monday</td><td class="sep">:</td><td>9:00am and 6pm</td></tr>
  <tr><td class="day">Tuesday</td><td class="sep">:</td><td>9:00am and 6pm</td></tr>
  <tr><td class="day">Wednesday</td><td class="sep">:</td><td>9:00am and 6pm</td></tr>
  <tr><td class="day">Thursday</td><td class="sep">:</td><td>9:00am and 6pm</td></tr>
  <tr><td class="day">Friday</td><td class="sep">:</td><td>9:00am and 6pm</td></tr>
  <tr><td class="day">Saturday</td><td class="sep">:</td><td>9:00am and 6pm</td></tr>
  <tr><td class="day">Sunday</td><td class="sep">:</td><td>9:00am and 6pm</td></tr>
</table>

<!-- footer -->
<footer class="abs footer"></footer>
<div class="abs foot-brand"><span class="foot-circle"></span>Cedar Brook Fellowship Church</div>
<div class="abs vline" style="left:311px"></div>
<div class="abs vline" style="left:503px"></div>
<div class="abs vline" style="left:850px"></div>

<h3 class="abs foot-head" style="left:354px">Information</h3>
<ul class="abs foot-links">
  <li>Home</li><li>Age Group</li><li>Activites</li><li>Events Calendar</li><li>About CBFC</li><li>Contact</li>
</ul>

<h3 class="abs foot-head" style="left:549px">Email Subscription</h3>
<p class="abs foot-text" style="left:549px;top:1995px;width:230px">Register your email address to get information about us</p>
<div class="abs sub-input">Email Address</div>
<div class="abs sub-btn">SUBSCRIBE</div>

<h3 class="abs foot-head" style="left:890px">Contact Us</h3>
<div class="abs contact-row" style="top:1998px">
  <svg width="10" height="14" viewBox="0 0 10 14"><path d="M5 0 C2 0 0 2.2 0 5 C0 8.5 5 14 5 14 C5 14 10 8.5 10 5 C10 2.2 8 0 5 0Z" fill="#fff"/><circle cx="5" cy="5" r="1.8" fill="#1b1b1b"/></svg>
  <span>PO Box 4127, Cedar Brook 6910<br>42-46 Willow Lane, Cedar Brook</span>
</div>
<div class="abs contact-row" style="top:2062px">
  <svg width="12" height="12" viewBox="0 0 12 12"><path d="M2.5 0.5 L4.5 3 L3.3 4.6 C4 6.2 5.8 8 7.4 8.7 L9 7.5 L11.5 9.5 L10 11.5 C5 11 1 7 0.5 2Z" fill="#fff"/></svg>
  <span>(08) 5550 1427 or 1300 555 018</span>
</div>
<div class="abs contact-row" style="top:2105px">
  <svg width="13" height="10" viewBox="0 0 13 10"><rect width="13" height="10" fill="#fff"/><path d="M0 0 L6.5 5.5 L13 0" fill="none" stroke="#1b1b1b" stroke-width="1.2"/></svg>
  <span>office@cedarbrookfellowship.org</span>
</div>

<div class="abs foot-rule"></div>
<p class="abs copyright">Copyrights © 2016, Cedar Brook Fellowship Church. All rights reserved.</p>
<span class="abs social" style="left:948px"></span>
<span class="abs social" style="left:989px"></span>
<span class="abs social" style="left:1030px"></span>
<span class="abs social" style="left:1070px"></span>

</body>
</html>
```